Qorvane Management LLC Business Card

The sample logo was attached for the business Card Design for Traffic Control Company named Qorvane Management LLC. Card design needs to have the company logo and colors match the logo color. It will be nice to show some images of Traffic control signs or cones, even roads closer that math the company services

Target Market(s)

Temporary traffic control. Road closer.

Industry/Entity Type

Construction

Contact Information for Business Card

basic information, name, job title, address, email phone, website

Font styles to use
Serif
Sans Serif

Colors
F0912C
F2A743
F7CA91
FBE8D2
FDF5EE
EE7325
F08F49
F5BC92
FAE3D3
FDF4ED

```html
<!DOCTYPE html>
<html lang="en">
<head>
<meta charset="utf-8">
<title>Qorvane Management LLC – Business Card</title>
<link rel="stylesheet" href="https://fonts.googleapis.com/css2?family=Montserrat:wght@500;600&family=Roboto:wght@400;700&display=swap">
<style>
  :root {
    --page: #ecebe8;
    --card-dark: #3b3b3d;
    --card-light: #ffffff;
    --accent: #ee7325;
    --stripe: #f03a1e;
    --text-light: #ffffff;
    --text-dark: #3b3b3d;
    --text-muted: #d9d9d9;
  }
  html, body {
    margin: 0;
    padding: 0;
    width: 1200px;
    height: 1200px;
    overflow: hidden;
    background: var(--page);
  }
  .sheet {
    width: 1200px;
    height: 1200px;
    display: flex;
    flex-direction: column;
    align-items: center;
    justify-content: center;
    gap: 60px;
  }
  .card {
    width: 880px;
    height: 500px;
    display: block;
    box-shadow: 0 8px 24px rgba(0,0,0,0.18);
  }
  .card-base { fill: var(--card-light); }
  .card-dark { fill: var(--card-dark); }
  .card-stripe { fill: var(--stripe); }
  .name-pill { fill: none; stroke: var(--accent); stroke-width: 4; }
  .pill-knot { fill: var(--card-dark); stroke: var(--accent); stroke-width: 4; }
  .icon-ring { fill: #fff; stroke: var(--accent); stroke-width: 3; }
  .icon-glyph { fill: var(--text-dark); }
  .holder-name { font-family: "Roboto", Arial, sans-serif; font-weight: 700; font-size: 30px; fill: var(--text-light); }
  .holder-role { font-family: "Roboto", Arial, sans-serif; font-weight: 400; font-size: 15px; fill: var(--text-muted); }
  .contact-line { font-family: "Roboto", Arial, sans-serif; font-weight: 400; font-size: 15px; fill: var(--text-dark); }
  .web-address { font-family: "Roboto", Arial, sans-serif; font-weight: 400; font-size: 22px; fill: var(--text-muted); }
  .company-name { font-family: "Montserrat", Arial, sans-serif; font-weight: 600; fill: var(--accent); }
</style>
</head>
<body>
<main class="sheet">

  <!-- Front: holder details -->
  <svg class="card card-front" viewBox="0 0 880 500" aria-label="Business card front">
    <rect class="card-base" width="880" height="500"/>
    <polygon class="card-stripe" points="580,0 612,0 456,250 612,500 580,500 450,250"/>
    <polygon class="card-dark" points="0,0 580,0 450,250 580,500 0,500"/>

    <rect class="name-pill" x="75" y="207" width="365" height="86" rx="43"/>
    <circle class="pill-knot" cx="450" cy="250" r="14"/>
    <text class="holder-name" x="257" y="254" text-anchor="middle">MS XXXX</text>
    <text class="holder-role" x="257" y="279" text-anchor="middle">Project Manager</text>

    <g class="contact-item">
      <circle class="icon-ring" cx="540" cy="180" r="26"/>
      <path class="icon-glyph" d="M540 166 L555 180 L550 180 L550 193 L544 193 L544 185 L536 185 L536 193 L530 193 L530 180 L525 180 Z"/>
      <text class="contact-line" x="584" y="176">Bay Plaza 7</text>
      <text class="contact-line" x="584" y="196">Room 2190</text>
    </g>
    <g class="contact-item">
      <circle class="icon-ring" cx="540" cy="250" r="26"/>
      <circle class="icon-glyph" cx="540" cy="250" r="11"/>
      <text class="contact-line" x="584" y="246">xxxx@qorvane-mgmt.com</text>
      <text class="contact-line" x="584" y="266">www.qorvane-mgmt.com</text>
    </g>
    <g class="contact-item">
      <circle class="icon-ring" cx="540" cy="320" r="26"/>
      <path class="icon-glyph" d="M527 313 Q540 304 553 313 L551 319 L546 317 L546 313 Q540 311 534 313 L534 317 L529 319 Z M529 321 L551 321 L553 333 L527 333 Z"/>
      <text class="contact-line" x="584" y="316">+1 555 0143 2290</text>
      <text class="contact-line" x="584" y="336">+1 555 0143 2290</text>
    </g>
  </svg>

  <!-- Back: company name and web address -->
  <svg class="card card-back" viewBox="0 0 880 500" aria-label="Business card back">
    <rect class="card-base" width="880" height="500"/>
    <polygon class="card-stripe" points="575,0 607,0 451,250 607,500 575,500 445,250"/>
    <polygon class="card-dark" points="0,0 575,0 445,250 575,500 0,500"/>

    <rect class="name-pill" x="75" y="209" width="355" height="82" rx="41"/>
    <circle class="pill-knot" cx="445" cy="250" r="14"/>
    <text class="web-address" x="253" y="258" text-anchor="middle">www.qorvane-mgmt.com</text>

    <text class="company-name" x="740" y="250" font-size="54" text-anchor="middle">Qorvane</text>
    <text class="company-name" x="740" y="290" font-size="22" text-anchor="middle">MANAGEMENT LLC</text>
  </svg>

</main>
</body>
</html>
```